Glamorous package design for flat irons

I need a professionally designed box for my crystal flat irons. I would for the design for be glamorous. The irons are covered in rhinestones and very sparkly. I would like the package design to equally stand out. The name of these irons are Bella Vera Starlit Posh Irons.

I attached images of the current packaging, The flat irons and an idea of the colors I like. It doesn't have to be this color if you have better ideas.

I attached more images of box designs that I like. I love the bright colors. The box can be simple with the name of the irons on the front Bella Vera Posh Irons and the information I have posted below on the back the box doesn't have to include a picture of the irons or my logo

Target Market(s)

18 - 45

Font styles to use
Script

Requirements
Must have
• ( BLING ) I want the box design to catch the eye.
• The information I would like on the back on the box
• This beautiful pink ceramic flat Iron is decorated with sparkling rhinestones. Each stone was hand applied with a special heat-proof glue. Bella Vera Posh Irons provides fast extraordinary straightening results quick heat up and constant heat.
• Features:
• Ceramic plate, 1" width
• 1 hour automatic cut-off
• Ion technology to maximize silky and shiny results
• Professional 360 swivel cord to prevent tangling
• Digital LCD display shows the operating situation on the clear and active screen
• Temperature: 50°C~232°C/ 122°F~450°F
• Press temperature button '+' and '-' to turn into Fahrenheit.
Nice to have
• Diamonds, or sparkles I want the box to look expensive. Metallic silver
Should not have
• I do not want an open window on the box. I don't want any photos of the irons on the box. I want the design to make the statement.

```html
<!DOCTYPE html>
<html lang="en">
<head>
<meta charset="utf-8">
<title>Bella Vera Starlit Posh Irons – Lid</title>
<link rel="stylesheet" href="https://fonts.googleapis.com/css2?family=Codystar:wght@400&family=Pinyon+Script&display=swap">
<style>
  :root {
    --stage: #6f6f6f;
    --stage-light: #8a8a8a;
    --pink-deep: #d9579a;
    --pink-mid: #e77fb3;
    --pink-light: #f6c3d8;
    --blush: #f3d3db;
    --silver-light: #f4f4f4;
    --silver-mid: #c9c9c9;
    --silver-dark: #6a6a6a;
    --label-pink: #d44ea0;
    --white: #ffffff;
  }
  html, body {
    margin: 0;
    padding: 0;
    width: 1200px;
    height: 1168px;
    overflow: hidden;
    background: radial-gradient(circle at 50% 50%, var(--stage-light), var(--stage));
  }
  .lid {
    display: block;
    width: 1200px;
    height: 1168px;
  }
  .lid-outline {
    fill: none;
    stroke: #3a3a3a;
    stroke-width: 3;
  }
  .dotted-heading {
    font-family: "Codystar", sans-serif;
    font-weight: 400;
    letter-spacing: 4px;
  }
  .heading-top {
    fill: var(--white);
    font-size: 118px;
  }
  .heading-bottom {
    fill: var(--label-pink);
    font-size: 84px;
  }
  .product-name {
    font-family: "Pinyon Script", cursive;
    font-size: 178px;
    fill: url(#silverFill);
    stroke: var(--silver-dark);
    stroke-width: 3;
    paint-order: stroke;
  }
  .bokeh { fill: var(--white); }
</style>
</head>
<body>
<svg class="lid" viewBox="0 0 1200 1168" xmlns="http://www.w3.org/2000/svg">
  <defs>
    <clipPath id="lidShape">
      <circle cx="600" cy="582" r="553"/>
    </clipPath>
    <radialGradient id="pinkGlow" cx="45%" cy="40%" r="75%">
      <stop offset="0" stop-color="var(--pink-light)"/>
      <stop offset="0.45" stop-color="var(--pink-mid)"/>
      <stop offset="1" stop-color="var(--pink-deep)"/>
    </radialGradient>
    <linearGradient id="topBlush" x1="0" y1="0" x2="0" y2="1">
      <stop offset="0" stop-color="var(--blush)" stop-opacity="0.9"/>
      <stop offset="1" stop-color="var(--blush)" stop-opacity="0"/>
    </linearGradient>
    <linearGradient id="silverBand" x1="0" y1="0" x2="1" y2="0">
      <stop offset="0" stop-color="#bdbdbd"/>
      <stop offset="0.5" stop-color="#d8d8d8"/>
      <stop offset="1" stop-color="#cfcfcf"/>
    </linearGradient>
    <linearGradient id="silverFill" x1="0" y1="0" x2="0" y2="1">
      <stop offset="0" stop-color="var(--silver-light)"/>
      <stop offset="0.5" stop-color="var(--silver-mid)"/>
      <stop offset="1" stop-color="#8d8d8d"/>
    </linearGradient>
  </defs>

  <g clip-path="url(#lidShape)">
    <rect class="lid-background" x="0" y="0" width="1200" height="1168" fill="url(#pinkGlow)"/>
    <rect class="lid-blush" x="0" y="0" width="1200" height="330" fill="url(#topBlush)"/>

    <g class="bokeh-lights" opacity="0.35">
      <circle class="bokeh" cx="820" cy="410" r="42"/>
      <circle class="bokeh" cx="1000" cy="560" r="60" opacity="0.5"/>
      <circle class="bokeh" cx="320" cy="700" r="50" opacity="0.6"/>
      <circle class="bokeh" cx="640" cy="520" r="70" opacity="0.4"/>
      <circle class="bokeh" cx="950" cy="760" r="80" opacity="0.4"/>
      <circle class="bokeh" cx="250" cy="300" r="55" opacity="0.4"/>
    </g>

    <text class="dotted-heading heading-top" x="526" y="190" text-anchor="middle" transform="rotate(180 526 228)">PROFESSIONAL IRONS</text>

    <text class="product-name" x="-230" y="690">Bella Vera Starlit Posh Irons</text>

    <path class="silver-band" d="M0 830 C 250 790, 420 775, 600 790 S 1000 870, 1200 900 L1200 1168 L0 1168 Z" fill="url(#silverBand)"/>
    <path class="silver-edge" d="M0 830 C 250 790, 420 775, 600 790 S 1000 870, 1200 900" fill="none" stroke="var(--white)" stroke-width="6"/>
    <path class="silver-edge-shade" d="M0 842 C 250 802, 420 787, 600 802 S 1000 882, 1200 912" fill="none" stroke="#9a9a9a" stroke-width="3"/>

    <text class="dotted-heading heading-bottom" x="215" y="1046">PROFESSIONAL IRONS</text>
  </g>

  <circle class="lid-outline" cx="600" cy="582" r="553"/>
</svg>
</body>
</html>
```